High end wine label at Austrian Winery

We are a traditional winery in Austria in region Burgenland. We are looking for a relaunch of our current wine label for our [vantor] series. It's a high end wine series at an upper price range. At the moment we have just two kinds of the label, one white one for the white wines and one black one for the red wines. This is a series of wine, white, red, sweet, sparkling and a top wine categories. So we need the same label, but in 4 different ways to distinguish the wines plus the sparkling. Maybe in color, patterns, ... or something else. The label should be very simple, including our new logo. It's also possible to make one label but we can splitting two parts of the label. The size of the label does not matter, need not be the same as now. It's a bit higher than a normal bottle. Additionally we need a back label with wine description and the wine dates on it.

Target Market(s)

private consumers and restaurants, no retailers

Colors

Designer to choose colors to be used in the design.

Requirements
Must have
• simple label with 4 different categories (red, white, sweet, top) plus Frizzante label, new logo integrated, high end label. Just logo, grape variety and [vantor] as text on the front label as text
Nice to have
• It's just good, if there'sa possibility to have different colors of each grape variety (about 10 different), but all the same style. top Wines should have an extraordinary design, but familiar with the others
Should not have
• no cheap look

```html
<!DOCTYPE html>
<html lang="en">
<head>
<meta charset="utf-8">
<title>Halden Vantor Label Series</title>
<link href="https://fonts.googleapis.com/css2?family=Cinzel:wght@400;500&family=Montserrat:wght@400;500;600&display=swap" rel="stylesheet">
<style>
  :root {
    --page: #ffffff;
    --label-white: #ffffff;
    --label-black: #272421;
    --label-edge: #d9d9d9;
    --ink-dark: #2b2b2b;
    --ink-soft: #6f6f6f;
    --ink-light: #f0ece6;
    --ink-light-soft: #bdb7ae;
    --motif-light: #efefef;
    --motif-dark: #2f2c29;
    --band-welschriesling: #fbf07f;
    --band-veltliner: #97c65f;
    --band-traminer: #f5c0c4;
    --band-pinot: #d3cfe8;
    --band-blaufrankisch: #b41e68;
    --band-blaufrankisch-reserve: #84231f;
    --band-cuvee: #7b2b7a;
  }
  * { margin: 0; padding: 0; box-sizing: border-box; }
  html, body { width: 1200px; height: 1000px; overflow: hidden; background: var(--page); }
  .sheet { position: relative; width: 1200px; height: 1000px; }

  .label {
    position: absolute;
    width: 174px;
    height: 414px;
    background: var(--label-white);
    border: 1px solid var(--label-edge);
    color: var(--ink-dark);
    font-family: "Montserrat", sans-serif;
  }
  .label--red { background: var(--label-black); border-color: var(--label-black); color: var(--ink-light); }

  .label__band {
    position: absolute;
    left: 57px; top: 0;
    width: 60px; height: 106px;
    display: flex; flex-direction: column; align-items: center; justify-content: flex-end;
    padding-bottom: 10px;
    gap: 8px;
  }
  .label__badge {
    width: 30px; height: 30px; border-radius: 50%;
    border: 1.5px solid var(--ink-dark);
  }
  .label--red .label__badge { border-color: var(--ink-light); }
  .label__brand {
    font-family: "Montserrat", sans-serif;
    font-weight: 600; font-size: 8px; letter-spacing: 1px;
    color: var(--ink-dark);
  }
  .label--red .label__brand { color: var(--ink-light); }

  .label__motif {
    position: absolute;
    left: 33px; top: 150px;
    width: 108px; height: 108px;
  }

  .label__variety {
    position: absolute; left: 0; right: 0;
    text-align: center;
    font-family: "Cinzel", serif;
    font-weight: 400;
    font-size: 14px; line-height: 16px;
    letter-spacing: 1.2px;
  }
  .label__variety small { display: block; font-size: 10px; line-height: 12px; letter-spacing: 1px; }
  .label__series {
    position: absolute; left: 0; right: 0;
    text-align: center;
    font-size: 6.5px; letter-spacing: 4px;
    color: var(--ink-soft);
  }
  .label--red .label__series { color: var(--ink-light-soft); }

  .label__origin {
    position: absolute; left: 0; right: 0; top: 357px;
    text-align: center;
    font-size: 6px; line-height: 8px; letter-spacing: 2.5px;
    color: var(--ink-soft);
  }
  .label--red .label__origin { color: var(--ink-light-soft); }
  .label__facts {
    position: absolute; left: 21px; right: 21px; top: 388px;
    display: flex; justify-content: space-between;
    font-size: 6.5px; letter-spacing: 0.3px;
    color: var(--ink-soft);
  }
  .label--red .label__facts { color: var(--ink-light-soft); }
</style>
</head>
<body>
<main class="sheet">

  <!-- White wines -->
  <article class="label" style="left:89px; top:46px;">
    <div class="label__band" style="background:var(--band-welschriesling)"><span class="label__badge"></span><span class="label__brand">HALDEN</span></div>
    <svg class="label__motif" viewBox="0 0 100 100" role="img" aria-label="Faint brand emblem decoration"><circle cx="50" cy="50" r="46" fill="var(--motif-light)"/></svg>
    <h2 class="label__variety" style="top:238px">WELSCHRIESLING</h2>
    <p class="label__series" style="top:257px">VANTOR</p>
    <p class="label__origin">AUSTRIA<br>BURGENLAND</p>
    <p class="label__facts"><span>12%VOL</span><span>750ML</span></p>
  </article>

  <article class="label" style="left:354px; top:46px;">
    <div class="label__band" style="background:var(--band-veltliner)"><span class="label__badge"></span><span class="label__brand">HALDEN</span></div>
    <svg class="label__motif" viewBox="0 0 100 100" role="img" aria-label="Faint brand emblem decoration"><circle cx="50" cy="50" r="46" fill="var(--motif-light)"/></svg>
    <h2 class="label__variety" style="top:222px">GRÜNER<br>VELTLINER</h2>
    <p class="label__series" style="top:257px">VANTOR</p>
    <p class="label__origin">AUSTRIA<br>BURGENLAND</p>
    <p class="label__facts"><span>12%VOL</span><span>750ML</span></p>
  </article>

  <article class="label" style="left:619px; top:46px;">
    <div class="label__band" style="background:var(--band-traminer)"><span class="label__badge"></span><span class="label__brand">HALDEN</span></div>
    <svg class="label__motif" viewBox="0 0 100 100" role="img" aria-label="Faint brand emblem decoration"><circle cx="50" cy="50" r="46" fill="var(--motif-light)"/></svg>
    <h2 class="label__variety" style="top:222px">SPÄTLESE<small>TRAMINER</small></h2>
    <p class="label__series" style="top:255px">VANTOR</p>
    <p class="label__origin">AUSTRIA<br>BURGENLAND</p>
    <p class="label__facts"><span>12%VOL</span><span>750ML</span></p>
  </article>

  <article class="label" style="left:884px; top:46px;">
    <div class="label__band" style="background:var(--band-pinot)"><span class="label__badge"></span><span class="label__brand">HALDEN</span></div>
    <svg class="label__motif" viewBox="0 0 100 100" role="img" aria-label="Faint brand emblem decoration"><circle cx="50" cy="50" r="46" fill="var(--motif-light)"/></svg>
    <h2 class="label__variety" style="top:238px">PINOT BLANC</h2>
    <p class="label__series" style="top:257px">VANTOR</p>
    <p class="label__origin">AUSTRIA<br>BURGENLAND</p>
    <p class="label__facts"><span>12%VOL</span><span>750ML</span></p>
  </article>

  <!-- Red wines -->
  <article class="label label--red" style="left:249px; top:527px;">
    <div class="label__band" style="background:var(--band-blaufrankisch)"><span class="label__badge"></span><span class="label__brand">HALDEN</span></div>
    <svg class="label__motif" viewBox="0 0 100 100" role="img" aria-label="Faint brand emblem decoration"><circle cx="50" cy="50" r="46" fill="var(--motif-dark)"/></svg>
    <h2 class="label__variety" style="top:238px">BLAUFRANKISCH</h2>
    <p class="label__series" style="top:257px">VANTOR</p>
    <p class="label__origin">AUSTRIA<br>BURGENLAND</p>
    <p class="label__facts"><span>12%VOL</span><span>750ML</span></p>
  </article>

  <article class="label label--red" style="left:514px; top:527px;">
    <div class="label__band" style="background:var(--band-blaufrankisch-reserve)"><span class="label__badge"></span><span class="label__brand">HALDEN</span></div>
    <svg class="label__motif" viewBox="0 0 100 100" role="img" aria-label="Faint brand emblem decoration"><circle cx="50" cy="50" r="46" fill="var(--motif-dark)"/></svg>
    <h2 class="label__variety" style="top:238px">BLAUFRANKISCH</h2>
    <p class="label__series" style="top:257px">VANTOR</p>
    <p class="label__origin">AUSTRIA<br>BURGENLAND</p>
    <p class="label__facts"><span>12%VOL</span><span>750ML</span></p>
  </article>

  <article class="label label--red" style="left:778px; top:527px;">
    <div class="label__band" style="background:var(--band-cuvee)"><span class="label__badge"></span><span class="label__brand">HALDEN</span></div>
    <svg class="label__motif" viewBox="0 0 100 100" role="img" aria-label="Faint brand emblem decoration"><circle cx="50" cy="50" r="46" fill="var(--motif-dark)"/></svg>
    <h2 class="label__variety" style="top:238px">SELEGD CUVEE</h2>
    <p class="label__series" style="top:257px">VANTOR</p>
    <p class="label__origin">AUSTRIA<br>BURGENLAND</p>
    <p class="label__facts"><span>12%VOL</span><span>750ML</span></p>
  </article>

</main>
</body>
</html>
```